Need UI Design for HRIS/Company Employee Portal

Currently have a custom built system that we hire and use as our employee database and employee portal for everyone in our company. The software has evolved dramatically and needs to be completely user friendly and aesthetically pleasing. Attached are a few ideas and pages we already have. Please make 5 designs for the 5 different pages below. Would need all specifications of content used, color code, font/typography, icons used, etc. We can pretty much pull any information from anywhere we have for example, employee photo, address, DOB, Hire date, Title, ETC.

-Company Staff/Admin Welcome Page
- We want quick shortcuts/buttons or icons for staff functions, such as terminate, hire, information change, reports, etc
-Employee Profile Welcome Page
- We want quick shortcuts/buttons or icons for direct deposit, time off request, information change, pay stubs
-List of Applications/Candidates Page
-Profile Search Page
-Manage Inventory

Target Market(s)

Employees

Industry/Entity Type

It Company

Coding

Coded - Design and coding required

Number of Pages Required

5+ page

Font styles to use
Sans Serif

Requirements
Must have
• Must be professional! Aesthetics, Icons, Easy User Interface, Modern New technology look, can be responsive to mobile
Should not have
• Nothing old school

```html
<!DOCTYPE html>
<html lang="en">
<head>
<meta charset="utf-8">
<title>Employee Portal – Profile</title>
<link rel="stylesheet" href="https://fonts.googleapis.com/css2?family=Lato:wght@400;700;900&display=swap">
<style>
  :root{
    --gold:#9f8600;
    --gold-bright:#f0c817;
    --blue:#1c46b4;
    --navy:#2a3f8c;
    --black:#000;
    --card:#ececec;
    --footer:#36332d;
    --text:#222;
    --label:#555;
    --msg-body:#eef4f7;
    --cal-dark:#3a3a3a;
    --cal-cell:#dcdcdc;
    --cal-today:#5aa9bd;
  }
  *{box-sizing:border-box;margin:0;padding:0}
  html,body{width:1200px;height:802px;overflow:hidden}
  body{font-family:"Lato",sans-serif;color:var(--text);
    background:radial-gradient(ellipse at center,#fafafa 55%,#dedede 100%);position:relative}
  .abs{position:absolute}

  .brand-rule{left:0;top:71px;width:420px;height:6px;
    background:linear-gradient(90deg,var(--gold-bright) 0,var(--gold-bright) 30%,rgba(240,200,23,.35) 70%,rgba(240,200,23,0) 100%)}
  .brand-mark{left:170px;top:22px;width:74px;height:74px;border-radius:50%;background:var(--navy)}
  .brand-name{left:252px;top:56px;font-weight:900;font-size:10px;color:var(--navy);letter-spacing:.6px}
  .brand-tag{left:276px;top:78px;font-weight:700;font-size:5.5px;color:#666;letter-spacing:3px}

  .main-nav{left:132px;top:111px;width:936px;height:39px;background:var(--gold)}
  .main-nav a{position:absolute;top:12px;color:#fff;text-decoration:none;font-size:13px}

  .profile-photo{left:132px;top:150px;width:209px;height:248px;
    background:linear-gradient(180deg,#e2e2e2 0%,#cfcfcf 45%,#8a7b70 70%,#1c1c1c 100%)}
  .profile-status{left:132px;top:398px;width:209px;height:99px;background:var(--blue);color:#fff;
    text-align:center;font-size:12px;line-height:22.5px;padding-top:13px}

  .permits-head{left:132px;top:501px;width:209px;height:48px;background:var(--black);color:#fff;
    font-weight:700;font-size:12.5px;text-align:center;line-height:48px}
  .permits{left:132px;top:549px;width:209px;height:202px;background:var(--gold)}
  .permit{position:absolute;left:67px;color:#fff}
  .permit h3{font-size:13px;font-weight:700}
  .permit small{display:block;font-size:8.5px;font-weight:700;margin-top:2px}
  .permit svg{position:absolute;left:-30px;top:0}

  .info-card{left:445px;top:170px;width:467px;height:304px;background:var(--card)}
  .info-row{position:absolute;left:0;width:467px;height:20px}
  .info-row .label{position:absolute;right:376px;top:0;font-size:12.5px;color:var(--label);white-space:nowrap}
  .info-row .value{position:absolute;left:122px;font-size:11.5px;white-space:nowrap}
  .info-row .value.name{left:119px;font-size:13px;color:#000;top:0}
  .rehire{left:805px;top:429px;width:86px;height:33px;background:var(--gold);color:#fff;
    font-size:12.5px;text-align:center;line-height:33px;border-radius:2px;box-shadow:0 1px 2px rgba(0,0,0,.25)}

  .message{left:443px;width:261px;height:85px;background:var(--msg-body);border:1px solid #c9d7e2;border-radius:2px}
  .message header{height:30px;background:var(--blue);color:#fff;font-size:12.5px;line-height:30px;padding-left:15px;position:relative}
  .message header span{position:absolute;right:12px;top:0;font-size:11px;letter-spacing:8px}
  .message p{font-size:8.6px;line-height:19px;padding:5px 0 0 16px;color:#111}

  .calendar{left:735px;top:501px;width:181px;height:176px;background:#fff;box-shadow:0 1px 3px rgba(0,0,0,.3)}
  .cal-head{height:30px;background:var(--cal-dark);color:#fff;font-weight:700;font-size:12px;text-align:center;line-height:30px;position:relative}
  .cal-head i{position:absolute;top:0;font-style:normal;font-size:8px}
  .cal-days,.cal-grid{display:grid;grid-template-columns:repeat(7,1fr)}
  .cal-days span{font-size:6px;text-align:center;line-height:16px;color:#444;background:#f1f1f1}
  .cal-grid span{height:26px;line-height:26px;text-align:center;font-size:10px;color:#333;
    background:var(--cal-cell);border-right:1px solid #c8c8c8;border-bottom:1px solid #c8c8c8}
  .cal-grid .muted{color:#aaa;background:#ececec}
  .cal-grid .today{background:var(--cal-today);color:#fff}

  .site-footer{left:0;top:760px;width:1200px;height:42px;background:var(--footer);color:#fff;font-size:9.5px}
  .site-footer span{position:absolute;top:15px}
</style>
</head>
<body>
  <div class="abs brand-rule"></div>
  <div class="abs brand-mark"></div>
  <div class="abs brand-name">SENTINEL SHIELD SERVICES, INC.</div>
  <div class="abs brand-tag">ARMED &amp; UNARMED SECURITY</div>

  <nav class="abs main-nav">
    <a style="left:74px">Home</a><a style="left:146px">Personal</a><a style="left:232px">Licenses</a>
    <a style="left:316px">Forms / Requests</a><a style="left:450px">Team Contacts</a><a style="left:570px">Benefits</a>
    <a style="left:653px">Training</a><a style="left:736px">Equipment</a><a style="left:834px">Help</a>
  </nav>

  <div class="abs profile-photo" role="img" aria-label="Employee portrait photo"></div>
  <div class="abs profile-status">Status : Lorium ipsum<br>Hire Date : 8-1-2000<br>17 Years</div>

  <div class="abs permits-head">CURRENT PERMITS</div>
  <section class="abs permits">
    <div class="permit" style="top:14px">
      <svg width="18" height="14" viewBox="0 0 18 14"><rect x="1" y="1" width="16" height="12" rx="1.5" fill="#fff"/><rect x="1" y="4" width="16" height="2.5" fill="#9f8600"/></svg>
      <h3>GUARD CARD</h3><small>( Red When Invalid)</small></div>
    <div class="permit" style="top:55px">
      <svg width="14" height="15" viewBox="0 0 14 15"><rect x="1" y="2" width="12" height="12" fill="none" stroke="#fff" stroke-width="1.5"/><path d="M1 5h12M4 0v3M10 0v3M4 8h2M8 8h2M4 11h2M8 11h2" stroke="#fff" stroke-width="1.5"/></svg>
      <h3>EXPIRING DATE</h3><small>( SSN : Last 4 Characters)</small></div>
    <div class="permit" style="top:104px">
      <svg width="20" height="20" viewBox="0 0 20 20" style="top:-3px;left:-32px"><circle cx="10" cy="10" r="9" fill="#d9c47a"/></svg>
      <h3>STATE ID</h3></div>
    <div class="permit" style="top:136px">
      <svg width="20" height="15" viewBox="0 0 20 15" style="left:-32px"><rect x="1" y="1" width="18" height="13" fill="none" stroke="#fff" stroke-width="1.6"/><rect x="4" y="4" width="5" height="7" fill="#fff"/><path d="M11 5h5M11 8h5M11 11h5" stroke="#fff" stroke-width="1.4"/></svg>
      <h3>DRIVERS LICENSE</h3><small>Expiry Date</small></div>
  </section>

  <section class="abs info-card">
    <div class="info-row" style="top:21px"><span class="label">Name :</span><span class="value name">Daniel Reyes</span></div>
    <div class="info-row" style="top:63px"><span class="label">Address :</span><span class="value" style="top:2px">2210 Cedar Ridge STE 140-212</span></div>
    <div class="info-row" style="top:104px"><span class="label">City :</span><span class="value" style="top:0">Maple Falls, TX</span></div>
    <div class="info-row" style="top:146px"><span class="label">Zip :</span><span class="value" style="top:3px">75980</span></div>
    <div class="info-row" style="top:188px"><span class="label">Phone :</span><span class="value" style="top:3px">91 - 412 7756 20</span></div>
    <div class="info-row" style="top:229px"><span class="label">Cell Phone :</span><span class="value" style="top:2px">91 - 412 7756 20</span></div>
    <div class="info-row" style="top:271px"><span class="label">Email :</span><span class="value" style="top:0">daniel@mailbox.com</span></div>
  </section>
  <div class="abs rehire">RE HIRE</div>

  <article class="abs message" style="top:500px">
    <header>Employee Special Message<span>‹›</span></header>
    <p>There are many variations of passages of Lorem Ipsum<br>available, but the majority have suffered alteration in</p>
  </article>
  <article class="abs message" style="top:593px">
    <header>Employee Special Message<span>‹›</span></header>
    <p>There are many variations of passages of Lorem Ipsum<br>available, but the majority have suffered alteration in</p>
  </article>

  <section class="abs calendar">
    <div class="cal-head"><i style="left:10px">◀</i>March 2011<i style="right:10px">▶</i></div>
    <div class="cal-days"><span>MON</span><span>TUE</span><span>WED</span><span>THU</span><span>FRI</span><span>SAT</span><span>SUN</span></div>
    <div class="cal-grid">
      <span class="muted">28</span><span>1</span><span>2</span><span>3</span><span class="today">4</span><span>5</span><span>6</span>
      <span>7</span><span>8</span><span>9</span><span>10</span><span>11</span><span>12</span><span>13</span>
      <span>14</span><span>15</span><span>16</span><span>17</span><span>18</span><span>19</span><span>20</span>
      <span>21</span><span>22</span><span>23</span><span>24</span><span>25</span><span>26</span><span>27</span>
      <span>28</span><span>29</span><span>30</span><span>31</span><span class="muted">1</span><span class="muted">2</span><span class="muted">3</span>
    </div>
  </section>

  <footer class="abs site-footer">
    <span style="left:846px">©2016 www.sentinelshield.com. All rights reserved.</span>
    <span style="left:1105px">M1</span>
  </footer>
</body>
</html>
```